Yoga for Scoliosis business card/logo design

I need a business card/logo design for my new business. I am a registered yoga teacher and am certified in yoga for scoliosis. I'd like my card to read "Marlow Yoga Yoga for a Healthy Spine" and would like to incorporate one of the letters in my name{ ie the first vertical line of the letter " H "or "D"} to resemble a scoliotic spine. I regularly teach the following:Yoga for Scoliosis, Yoga for Back Health, Hatha yoga, Vinyasa yoga with Iyengar style alignment. This business is mostly for private clients, but I also teach group, semi-private & work shop classes. I like the colors green (light emerald) and royal blue. I'd like the design to be somewhat sleek, but not too modern. I also like the idea of a ying/yang symbol with a scoliotic spine dviding it.

Industry/Entity Type

Teacher

Contact Information for Business Card

Tamsin Marlow
200 RYT, Certified Yoga for Scoliosis Instructor
MarlowYoga.example
MarlowYoga@mailbox.example
415-629-3174

```html
<!DOCTYPE html>
<html lang="en">
<head>
<meta charset="utf-8">
<title>Marlow Yoga – Business Card</title>
<link href="https://fonts.googleapis.com/css2?family=Federo&family=Open+Sans:wght@400;600;700&display=swap" rel="stylesheet">
<style>
  :root {
    --page-bg: #3a2f30;
    --card-white: #ffffff;
    --royal-blue: #27389a;
    --royal-blue-deep: #1d2b7e;
    --emerald: #3cc197;
    --emerald-soft: #5fd1ab;
    --navy-ink: #1f2d85;
    --text-light: #ffffff;
  }
  * { box-sizing: border-box; margin: 0; padding: 0; }
  html, body {
    width: 1200px;
    height: 800px;
    overflow: hidden;
  }
  body {
    background: var(--page-bg);
    position: relative;
    font-family: "Open Sans", Arial, sans-serif;
  }
  .card {
    position: absolute;
    left: 100px;
    top: 114px;
    width: 1000px;
    height: 572px;
    background: var(--card-white);
    overflow: hidden;
    box-shadow: 0 18px 40px rgba(0,0,0,0.45);
  }
  .card__wave {
    position: absolute;
    inset: 0;
    width: 100%;
    height: 100%;
  }
  .brand__mark {
    position: absolute;
    left: 60px;
    top: 140px;
    width: 220px;
    height: 220px;
    border-radius: 50%;
    background: radial-gradient(circle at 35% 35%, var(--emerald-soft), var(--emerald) 60%, var(--royal-blue-deep) 100%);
  }
  .brand__text {
    position: absolute;
    left: 305px;
    top: 150px;
  }
  .brand__name {
    font-family: "Federo", "Open Sans", sans-serif;
    font-size: 60px;
    font-weight: 400;
    color: var(--navy-ink);
    line-height: 1;
    white-space: nowrap;
  }
  .brand__tagline {
    font-size: 17px;
    letter-spacing: 4px;
    color: var(--emerald);
    margin-top: 6px;
    white-space: nowrap;
  }
  .contact {
    position: absolute;
    left: 600px;
    top: 298px;
    color: var(--text-light);
  }
  .contact__name {
    font-size: 26px;
    font-weight: 700;
    color: var(--emerald);
    line-height: 1.2;
  }
  .contact__title {
    font-size: 15px;
    margin-top: 2px;
    white-space: nowrap;
  }
  .contact__list {
    list-style: none;
    margin-top: 16px;
    padding-left: 60px;
  }
  .contact__item {
    display: flex;
    align-items: center;
    gap: 8px;
    font-size: 19px;
    line-height: 1.4;
    white-space: nowrap;
  }
  .contact__item--phone { font-size: 28px; }
  .contact__icon { width: 18px; height: 18px; flex: none; }
</style>
</head>
<body>
  <section class="card" aria-label="Marlow Yoga business card">
    <svg class="card__wave" viewBox="0 0 1000 572" preserveAspectRatio="none" aria-hidden="true">
      <defs>
        <linearGradient id="blueFill" x1="0" y1="1" x2="1" y2="0">
          <stop offset="0" stop-color="#1d2b7e"/>
          <stop offset="0.5" stop-color="#2a3fa5"/>
          <stop offset="1" stop-color="#213289"/>
        </linearGradient>
      </defs>
      <path d="M470,315 C640,255 800,170 845,0 L905,0 C860,140 720,230 470,315 Z" fill="#3cc197"/>
      <path d="M120,572 C250,390 480,320 620,270 C780,215 880,130 925,0 L1000,0 L1000,572 Z" fill="url(#blueFill)" stroke="#ffffff" stroke-width="6"/>
    </svg>

    <div class="brand__mark" role="img" aria-label="Logo emblem area"></div>
    <div class="brand__text">
      <h1 class="brand__name">Marlow Yoga</h1>
      <p class="brand__tagline">Yoga for a Healthy Spine</p>
    </div>

    <div class="contact">
      <h2 class="contact__name">Tamsin Marlow</h2>
      <p class="contact__title">200 RYT, Certified Yoga for Scoliosis Instructor</p>
      <ul class="contact__list">
        <li class="contact__item contact__item--phone">
          <svg class="contact__icon" viewBox="0 0 24 24" aria-hidden="true"><path fill="#3cc197" d="M6.6 10.8c1.4 2.8 3.8 5.1 6.6 6.6l2.2-2.2c.3-.3.7-.4 1-.2 1.1.4 2.3.6 3.6.6.6 0 1 .4 1 1V20c0 .6-.4 1-1 1C10.6 21 3 13.4 3 4c0-.6.4-1 1-1h3.5c.6 0 1 .4 1 1 0 1.3.2 2.5.6 3.6.1.3 0 .7-.2 1l-2.3 2.2z"/></svg>
          415-629-3174
        </li>
        <li class="contact__item">
          <svg class="contact__icon" viewBox="0 0 24 24" aria-hidden="true"><circle cx="12" cy="12" r="9" fill="none" stroke="#3cc197" stroke-width="2"/><path d="M3 12h18M12 3c3 3 3 15 0 18M12 3c-3 3-3 15 0 18" fill="none" stroke="#3cc197" stroke-width="1.6"/></svg>
          MarlowYoga.example
        </li>
        <li class="contact__item">
          <svg class="contact__icon" viewBox="0 0 24 24" aria-hidden="true"><rect x="2" y="5" width="20" height="14" rx="2" fill="#3cc197"/><path d="M3 6l9 7 9-7" fill="none" stroke="#27389a" stroke-width="1.8"/></svg>
          MarlowYoga@mailbox.example
        </li>
      </ul>
    </div>
  </section>
</body>
</html>
```